Disability Service Provider Website

We are working with VEP, which provides services and job training designed to educate, facilitate, train, and assist individuals with disabilities. They describe their clients using words like Unity and Unique.
Some sites to use for content/competitors and inspiration:
https://www.skillmora.com
https://www.pwkd.org
https://www.bellowhaven.org
https://www.openmeadow.org
https://corvelan.org
Thank you for taking the time to consider designing a website for us. We are web developers based in Stockton, CA, USA. Most of our projects go through the same process. Understanding this process may help you win a project with us. We custom-code all of our websites in-house. We don’t have any requirements as to what tools you use for your design, but we prefer Figma files. For any design that we label as four-stars, we send it to the client for review. The client picks the final design they want us to use. Once we complete this process, we will continue to show additional clients all the four-star sites and purchase them later. Your designs will have multiple chances to sell. For better chances of success, we ask that you follow these guidelines.
IMAGES:
If you use any images or icons in the design, we ask that you have a link to the asset so we can purchase the image/icon. Most of the designs we submit do not have the customer’s images on them unless they have some great images. Be creative; show us the feeling you are trying to portray with your image choices. Use any royalty-free site you choose. We subscribe to Stellic and mainly use their images, but we can purchase images outside of Stellic.
PLEASE NOTE: we will not submit designs to clients with watermarks on the images.
FONTS:
We ask that you identify the fonts used in the design. This can be done in a message if you want. We typically use Bramble Fonts and Stellic Fonts.
CONTENT:
We're always open to different content and ideas. We often submit designs with stock images so the client can see our vision. We typically take pictures after the website launch to use their images with our vision. Lorem Ipsum is fine for paragraphs, but we ask that you write the headers in correct English. We want to be able to show the vision and identify the sections of the website.
INSPIRATION:
We typically add a couple of links in the brief of websites we like to help you get started in your design.
REVISIONS:
We do not often ask for revisions of the designs unless we see something in the design that may not appeal to the client. If there are slight changes that we want to make, we do that in the development process.
FEEDBACK:
We rarely give feedback on designs during the design process. We are working on many website projects and do not have the time to provide feedback. We usually respond if your request is well thought out and asks specific questions, but a note asking “feedback, please” usually goes unanswered.
Number of Pages Required
1 page
Look and feel
Each slider illustrates characteristics of the customer's brand and the style your logo design should communicate.

```html
<!DOCTYPE html>
<html lang="en">
<head>
<meta charset="utf-8">
<title>VEP — Skills Training</title>
<link rel="stylesheet" href="https://fonts.googleapis.com/css2?family=Noto+Sans:wght@400;500;600;700&display=swap">
<style>
:root{
  --navy:#0e1d4d;
  --navy-deep:#0a1433;
  --red:#8a0b16;
  --red-bright:#a3101d;
  --orange:#f2a23a;
  --teal:#3b8fae;
  --ink:#333a48;
  --muted:#8a8f99;
  --cream:#f7f5ef;
  --steps-bg:#e8edf4;
  --white:#ffffff;
}
*{box-sizing:border-box;margin:0;padding:0}
html,body{width:1200px;height:4188px;overflow:hidden}
body{position:relative;font-family:"Noto Sans",sans-serif;color:var(--ink);background:var(--white)}
.abs{position:absolute}
.btn{position:absolute;display:flex;align-items:center;justify-content:center;gap:10px;font-weight:700;color:var(--white);font-size:14px}
.eyebrow{position:absolute;left:0;width:100%;text-align:center;font-size:13px;color:var(--red);text-transform:uppercase}
.eyebrow span{border-bottom:2px solid var(--red);padding-bottom:3px}
.section-title{position:absolute;left:0;width:100%;text-align:center;font-weight:600;color:var(--navy);font-size:42px}

/* header */
.topbar{left:385px;top:0;width:815px;height:33px;background:var(--navy);clip-path:polygon(22px 0,100% 0,100% 100%,0 100%)}
.topbar-item{position:absolute;top:0;height:33px;display:flex;align-items:center;gap:8px;color:var(--white);font-size:11px;font-weight:600}
.topbar-cta{left:207px;width:232px;background:var(--red);justify-content:center}
.logo{left:135px;top:14px;font-size:58px;font-weight:700;color:var(--red);letter-spacing:1px;line-height:1}
.nav{top:60px;font-size:12px;font-weight:600;color:#3c4250}
.nav-contact{left:930px;top:52px;width:119px;height:31px;border:2px solid var(--orange);border-radius:4px;color:var(--orange);font-size:11px;display:flex;align-items:center;justify-content:center}

/* hero */
.hero{left:0;top:95px;width:1200px;height:680px;overflow:hidden}
.hero-photo{position:absolute;inset:0;background:linear-gradient(100deg,#d7cfc4 0%,#b79b7d 40%,#6f7b86 70%,#3e4a55 100%)}
.hero-fade{position:absolute;inset:0;background:linear-gradient(90deg,rgba(255,255,255,.97) 0%,rgba(255,255,255,.9) 35%,rgba(255,255,255,.3) 60%,rgba(255,255,255,0) 80%)}
.hero-kicker{left:124px;top:266px;font-size:20px;font-weight:600;letter-spacing:6px;color:var(--navy-deep)}
.hero-title{left:118px;top:300px;font-size:70px;font-weight:700;color:var(--navy)}
.hero-rule{left:124px;top:401px;width:474px;height:3px;background:var(--red)}
.hero-text{left:124px;top:424px;width:520px;font-size:16px;line-height:28px;color:#2a2f3a}
.hero-wave{left:0;top:690px;width:1200px;height:90px}

/* who we are */
.about-photo{left:120px;top:973px;width:495px;height:339px;border-radius:10px;background:linear-gradient(90deg,#c7b6a4 0%,#a8563f 45%,#d9d3cb 70%,#4d4a45 100%)}
.about-card{left:561px;top:998px;width:517px;height:306px;background:var(--cream);border-radius:8px;padding:50px 32px 0 37px}
.about-card h3{font-size:19px;font-weight:500;color:#1d2433;margin-bottom:18px}
.about-card p{font-size:12px;line-height:19.5px;color:var(--muted);margin-bottom:10px}
.btn-red{background:var(--red);border-radius:3px}

/* services */
.services{left:0;top:1416px;width:1200px;height:556px;background:linear-gradient(135deg,#4a4f57 0%,#2b2f36 50%,#3c3f45 100%)}
.service-card{position:absolute;top:189px;width:304px;height:228px;overflow:hidden}
.service-card.featured{background:linear-gradient(135deg,rgba(190,20,35,.92),rgba(150,10,22,.92));color:var(--white);text-align:center;padding:76px 40px 0}
.service-card.featured h3{font-size:17px;font-weight:600;margin-bottom:8px}
.service-card.featured p{font-size:13px;line-height:21px}
.service-photo{position:absolute;inset:0}
.service-shade{position:absolute;inset:0;background:linear-gradient(180deg,rgba(0,0,0,0) 45%,rgba(0,0,0,.75) 100%)}
.service-body{position:absolute;left:84px;top:162px;color:var(--white)}
.service-body h3{font-size:15px;font-weight:600;margin-bottom:6px}
.service-body p{font-size:12.5px}
.service-icon{position:absolute;left:34px;top:166px}

/* steps */
.steps{left:0;top:1972px;width:1200px;height:500px;background:var(--steps-bg)}
.step{position:absolute;top:111px;width:240px;text-align:center}
.step h3{position:absolute;top:240px;width:100%;font-size:18px;font-weight:600;color:var(--navy)}
.step p{position:absolute;top:270px;width:100%;font-size:13px;line-height:21px;color:var(--muted)}

/* why us */
.why{left:0;top:2471px;width:1200px;height:576px;overflow:hidden;background:linear-gradient(120deg,#5b5e63 0%,#34373d 50%,#24272c 100%)}
.why-photo{position:absolute;inset:0;background:linear-gradient(90deg,#c9cfd4 0%,#a9b0b6 30%,#2b2d33 50%,#b38a64 60%);clip-path:polygon(0 0,382px 0,667px 100%,0 100%)}
.why-kicker{left:636px;top:96px;font-size:12px;color:var(--red-bright);text-transform:uppercase}
.why-title{left:636px;top:118px;font-size:39px;line-height:47px;font-weight:600;color:var(--white)}
.feature{position:absolute;left:630px;display:flex;align-items:center;gap:14px;color:var(--white)}
.feature-icon{width:62px;height:62px;border-radius:50%;background:var(--white);display:flex;align-items:center;justify-content:center}
.feature h4{font-size:19px;font-weight:600}
.feature p{font-size:12.5px;color:#e3e3e3}

/* testimonials */
.quote{left:0;top:3378px;width:100%;text-align:center;font-size:15px;line-height:22.5px;color:#2f3440}
.avatar{position:absolute;border-radius:50%;border:3px solid #fff;box-shadow:0 3px 10px rgba(0,0,0,.2)}
.arrow{position:absolute;top:3542px;width:43px;height:43px;border-radius:50%;display:flex;align-items:center;justify-content:center}

/* footer */
.footer{left:0;top:3755px;width:1200px;height:376px;background:var(--navy-deep)}
.footer-logo{left:0;top:73px;width:100%;text-align:center;font-size:78px;font-weight:700;color:var(--white);line-height:1}
.footer-nav{position:absolute;top:193px;font-size:15px;color:var(--white);text-transform:uppercase}
.footer-rule{left:142px;top:245px;width:918px;height:1px;background:#3a4565}
.footer-contact{position:absolute;top:280px;display:flex;align-items:center;gap:13px;color:var(--white);font-size:12px;line-height:19px}
.footer-contact .ring{width:52px;height:52px;border:2px solid #c5c9d4;border-radius:50%;display:flex;align-items:center;justify-content:center}
.footer-divider{position:absolute;top:275px;width:1px;height:58px;background:#58617c}
.bottom-bar{left:0;top:4130px;width:1200px;height:58px;background:var(--red);color:var(--white)}
.social{position:absolute;top:17px;width:24px;height:24px;border:1.5px solid var(--white);border-radius:3px}
</style>
</head>
<body>

<!-- header -->
<div class="abs topbar">
  <div class="topbar-item" style="left:60px">
    <svg width="15" height="15" viewBox="0 0 24 24" fill="none" stroke="#fff" stroke-width="2"><path d="M5 3h4l2 5-3 2a12 12 0 0 0 6 6l2-3 5 2v4a2 2 0 0 1-2 2A18 18 0 0 1 3 5a2 2 0 0 1 2-2z"/></svg>
    555 - 014 - 2283
  </div>
  <div class="topbar-item topbar-cta">
    <svg width="14" height="14" viewBox="0 0 24 24" fill="none" stroke="#fff" stroke-width="2"><rect x="3" y="5" width="18" height="16" rx="2"/><path d="M3 10h18M8 3v4M16 3v4"/></svg>
    REQUEST AN APPOINTMENT
  </div>
  <div class="topbar-item" style="left:472px">
    <svg width="13" height="15" viewBox="0 0 24 24" fill="none" stroke="#fff" stroke-width="2"><path d="M12 22s7-7 7-12a7 7 0 0 0-14 0c0 5 7 12 7 12z"/><circle cx="12" cy="10" r="2.5"/></svg>
    1234 Elm Street Anywhere
  </div>
</div>
<div class="abs logo">VEP</div>
<div class="abs nav" style="left:395px">Home</div>
<div class="abs nav" style="left:470px">About Us</div>
<div class="abs nav" style="left:545px">Solutions</div>
<div class="abs nav" style="left:620px">Projects</div>
<div class="abs nav" style="left:726px">Our Team</div>
<div class="abs nav-contact">CONTACT US</div>

<!-- hero -->
<section class="abs hero">
  <div class="hero-photo" role="img" aria-label="Photo of a smiling man in a wheelchair working on a laptop beside a colleague in a bright office"></div>
  <div class="hero-fade"></div>
</section>
<div class="abs hero-kicker">Experts in</div>
<h1 class="abs hero-title">Skills Training</h1>
<div class="abs hero-rule"></div>
<p class="abs hero-text">Lorem ipsum dolor sit amet, consectetur adipiscing elit, sed do eiusmod tempor incididunt ut labore</p>
<div class="btn btn-red" style="left:125px;top:511px;width:145px;height:41px;border-radius:21px">LEARN MORE</div>
<div class="btn" style="left:281px;top:511px;width:180px;height:41px;border-radius:21px;background:#000">REQUEST QUOTE</div>
<svg class="abs hero-wave" viewBox="0 0 1200 90" preserveAspectRatio="none">
  <path d="M0 38 C250 0 500 15 700 45 C900 75 1080 55 1200 12 L1200 90 L0 90 Z" fill="#8a0b16"/>
  <path d="M0 48 C250 10 500 20 700 50 C900 78 1080 62 1200 40 L1200 90 L0 90 Z" fill="#ffffff"/>
</svg>

<!-- who we are -->
<div class="eyebrow" style="top:845px"><span>Who we are</span></div>
<h2 class="section-title" style="top:880px">Embracing Uniqueness, Building Unity</h2>
<div class="abs about-photo" role="img" aria-label="Photo of a bearded man in a flat cap writing notes while seated"></div>
<div class="abs about-card">
  <h3>Empowerment through Opportunity Inclusion</h3>
  <p>Lorem ipsum dolor sit amet, consectetur adipiscing elit, sed do eiusmod temp or incididunt ut labore et dolore magna aliqua. Ut enim ad minim veniam, quis laboris nisi ut aliquip ex ea commodo consequat.</p>
  <p>Lorem ipsum dolor sit amet, consectetur adipiscing elit, sed do eiusmod temp or incididunt ut labore et dolore magna aliqua.</p>
</div>
<div class="btn btn-red" style="left:602px;top:1227px;width:137px;height:38px">Contact us
  <svg width="16" height="12" viewBox="0 0 16 12" fill="none" stroke="#fff" stroke-width="1.6"><path d="M0 6h15M10 1l5 5-5 5"/></svg></div>

<!-- services -->
<section class="abs services" role="img" aria-label="Dark toned background photo of people meeting around a table">
  <div class="eyebrow" style="top:57px;color:#fff"><span style="border-color:#fff">Our services</span></div>
  <h2 class="section-title" style="top:93px;color:#fff">Services We Provide</h2>
  <div class="service-card featured" style="left:119px">
    <h3>Skills Training</h3>
    <p>Lorem ipsum dolor sit amet, con sectetur adipiscing elit, sed do eiusmod tempor</p>
    <svg style="margin-top:14px" width="28" height="14" viewBox="0 0 28 14" fill="none" stroke="#fff" stroke-width="1.8"><path d="M0 7h26M20 1l6 6-6 6"/></svg>
  </div>
  <div class="service-card" style="left:447px">
    <div class="service-photo" role="img" aria-label="Photo of two young people laughing together on a sofa" style="background:linear-gradient(135deg,#e3e6ea,#9fa7b2 50%,#3e4c63)"></div>
    <div class="service-shade"></div>
    <svg class="service-icon" width="30" height="30" viewBox="0 0 24 24" fill="none" stroke="#c41426" stroke-width="1.5"><path d="M5 19h14M8 15l7-9 3 2-7 9H8z"/></svg>
    <div class="service-body"><h3>Wellness Programs</h3><p>Inventore veritasis uas vite</p></div>
  </div>
  <div class="service-card" style="left:776px">
    <div class="service-photo" role="img" aria-label="Photo of a smiling woman in a pink blazer outside an office building" style="background:linear-gradient(135deg,#c9ccd0,#8a6a6f 50%,#3a3a40)"></div>
    <div class="service-shade"></div>
    <svg class="service-icon" width="30" height="30" viewBox="0 0 24 24" fill="none" stroke="#c41426" stroke-width="1.5"><path d="M12 3l2.6 5.5 6 .8-4.4 4.2 1.1 6-5.3-3-5.3 3 1.1-6L3.4 9.3l6-.8z"/></svg>
    <div class="service-body"><h3>Job Placement</h3><p>Inventore veritasis uas vite</p></div>
  </div>
  <div class="btn btn-red" style="left:547px;top:466px;width:136px;height:38px;border-radius:2px">Contact us
    <svg width="16" height="12" viewBox="0 0 16 12" fill="none" stroke="#fff" stroke-width="1.6"><path d="M0 6h15M10 1l5 5-5 5"/></svg></div>
</section>

<!-- steps -->
<section class="abs steps">
  <div class="eyebrow" style="top:72px"><span>Steps to take</span></div>
  <h2 class="section-title" style="top:107px">Steps To Take</h2>
  <svg class="abs" style="left:0;top:200px" width="1200" height="140" viewBox="0 0 1200 140">
    <path d="M338 65H540M654 65H854" stroke="#3b8fae" stroke-width="2"/>
    <g fill="none" stroke="#3b8fae" stroke-width="2">
      <circle cx="281" cy="65" r="57"/><circle cx="597" cy="65" r="57"/><circle cx="911" cy="65" r="57"/>
    </g>
    <g fill="#0e1d4d"><circle cx="281" cy="65" r="48"/><circle cx="597" cy="65" r="48"/><circle cx="911" cy="65" r="48"/></g>
    <g fill="none" stroke="#fff" stroke-width="2.2">
      <path d="M265 82h32M270 77l14-20 5 4-11 16z"/>
      <path d="M581 82h32M586 77l14-20 5 4-11 16z"/>
      <path d="M895 82h32M900 77l14-20 5 4-11 16z"/>
    </g>
    <g fill="#8a0b16"><circle cx="337" cy="65" r="13"/><circle cx="653" cy="65" r="13"/><circle cx="967" cy="65" r="13"/></g>
    <g fill="#fff" font-family="Noto Sans, sans-serif" font-size="11" font-weight="700" text-anchor="middle">
      <text x="337" y="69">01</text><text x="653" y="69">02</text><text x="967" y="69">03</text>
    </g>
  </svg>
  <div class="step" style="left:161px"><h3>Contact Us to Start</h3><p>Lorem ipsum dolor sit amet, consectetur adipiscing elit, sed do eiusmo</p></div>
  <div class="step" style="left:477px"><h3>Get assigned an expert</h3><p>Lorem ipsum dolor sit amet, consectetur adipiscing elit, sed do eiusmo</p></div>
  <div class="step" style="left:791px"><h3>Start the Sessions</h3><p>Lorem ipsum dolor sit amet, consectetur adipiscing elit, sed do eiusmo</p></div>
</section>

<!-- why us -->
<section class="abs why" role="img" aria-label="Dark toned background photo of a team meeting">
  <div class="why-photo" role="img" aria-label="Photo of a smiling professional woman with crossed arms in a bright office"></div>
  <div class="abs why-kicker">Why choose us</div>
  <h2 class="abs why-title">Navigating Challenges,<br>Unlocking Opportunities</h2>
  <div class="feature" style="top:235px">
    <div class="feature-icon"><svg width="28" height="28" viewBox="0 0 24 24" fill="none" stroke="#8a0b16" stroke-width="1.6"><path d="M5 19h14M8 15l7-9 3 2-7 9H8z"/></svg></div>
    <div><h4>On-Time Appointments</h4><p>Inventore veritasis uasvitae dicta suntetur sipid</p></div>
  </div>
  <div class="feature" style="top:315px">
    <div class="feature-icon"><svg width="28" height="28" viewBox="0 0 24 24" fill="none" stroke="#8a0b16" stroke-width="1.6"><path d="M4 15v-3a8 8 0 0 1 16 0v3"/><rect x="3" y="14" width="4" height="6" rx="1"/><rect x="17" y="14" width="4" height="6" rx="1"/></svg></div>
    <div><h4>Experienced Professionals</h4><p>Inventore veritasis uasvitae dicta suntetur sipid</p></div>
  </div>
  <div class="feature" style="top:398px">
    <div class="feature-icon"><svg width="28" height="28" viewBox="0 0 24 24" fill="none" stroke="#8a0b16" stroke-width="1.6"><path d="M12 3l2.6 5.5 6 .8-4.4 4.2 1.1 6-5.3-3-5.3 3 1.1-6L3.4 9.3l6-.8z"/></svg></div>
    <div><h4>Confidentiality</h4><p>Inventore veritasis uasvitae dicta suntetur sipid</p></div>
  </div>
</section>

<!-- testimonials -->
<div class="eyebrow" style="top:3192px;font-size:17px"><span style="border:0">Testimonials</span></div>
<h2 class="section-title" style="top:3220px;font-size:33px">What Our Clients are Saying</h2>
<svg class="abs" style="left:568px;top:3303px" width="60" height="60" viewBox="0 0 60 60">
  <circle cx="30" cy="30" r="30" fill="#8a0b16"/>
  <path d="M19 23h9v9l-4 8h-4l3-8h-4zM32 23h9v9l-4 8h-4l3-8h-4z" fill="#fff"/>
</svg>
<p class="abs quote">Lorem ipsum dolor sit amet, consectetur adipiscing elit, sed do eiusmod tempor incidi<br>dunt ut labore et dolore magna aliqua .dipiscing elit, sed do eiusmod tempor incidi<br>dunt ut labore et dolore magna aliqua .dipiscing elit, sed<br>do eiusmod tempor incididunt</p>
<div class="abs" style="left:0;top:3483px;width:100%;text-align:center;font-size:13px;color:var(--orange)">Dana Morell</div>
<div class="abs" style="left:0;top:3504px;width:100%;text-align:center;font-size:10px;color:#222">Client</div>
<div class="arrow" style="left:548px;background:var(--navy-deep)"><svg width="20" height="14" viewBox="0 0 20 14" fill="none" stroke="#fff" stroke-width="1.8"><path d="M20 7H2M8 1L2 7l6 6"/></svg></div>
<div class="arrow" style="left:602px;background:var(--red-bright)"><svg width="20" height="14" viewBox="0 0 20 14" fill="none" stroke="#fff" stroke-width="1.8"><path d="M0 7h18M12 1l6 6-6 6"/></svg></div>
<div class="avatar" role="img" aria-label="Client portrait" style="left:241px;top:3302px;width:60px;height:60px;background:#b7bfcc"></div>
<div class="avatar" role="img" aria-label="Client portrait" style="left:90px;top:3357px;width:104px;height:104px;background:#5a6370"></div>
<div class="avatar" role="img" aria-label="Client portrait" style="left:263px;top:3422px;width:42px;height:42px;background:#c9b9a8"></div>
<div class="avatar" role="img" aria-label="Client portrait" style="left:173px;top:3494px;width:82px;height:82px;background:#3d5a7a"></div>
<div class="avatar" role="img" aria-label="Client portrait" style="left:892px;top:3315px;width:50px;height:50px;background:#8c7d70"></div>
<div class="avatar" role="img" aria-label="Client portrait" style="left:1002px;top:3344px;width:106px;height:106px;background:#a9b3c0"></div>
<div class="avatar" role="img" aria-label="Client portrait" style="left:895px;top:3428px;width:58px;height:58px;background:#6f8aa6"></div>
<div class="avatar" role="img" aria-label="Client portrait" style="left:995px;top:3497px;width:80px;height:80px;background:#b9b3ab"></div>

<!-- footer -->
<svg class="abs" style="left:0;top:3680px" width="1200" height="100" viewBox="0 0 1200 100" preserveAspectRatio="none">
  <path d="M0 80 C200 30 420 30 620 60 C820 92 1020 70 1200 10 L1200 100 L0 100 Z" fill="#8a0b16"/>
  <path d="M0 100 C200 52 420 50 620 80 C820 105 1020 85 1200 40 L1200 100 Z" fill="#0a1433"/>
</svg>
<footer class="abs footer">
  <div class="abs footer-logo">VEP</div>
  <div class="footer-nav" style="left:296px">Home</div>
  <div class="footer-nav" style="left:390px">Services</div>
  <div class="footer-nav" style="left:496px">About us</div>
  <div class="footer-nav" style="left:615px">Testimonials</div>
  <div class="footer-nav" style="left:765px">Blog</div>
  <div class="abs footer-rule"></div>
  <div class="footer-contact" style="left:142px">
    <div class="ring"><svg width="28" height="28" viewBox="0 0 24 24" fill="none" stroke="#fff" stroke-width="1.3"><circle cx="12" cy="12" r="9"/><path d="M3 12h18M12 3c3 3 3 15 0 18M12 3c-3 3-3 15 0 18"/></svg></div>
    <div>123, Building Name, Street<br>City, State XY 123456</div>
  </div>
  <div class="footer-divider" style="left:398px"></div>
  <div class="footer-contact" style="left:474px">
    <div class="ring"><svg width="24" height="28" viewBox="0 0 24 24" fill="none" stroke="#fff" stroke-width="1.3"><rect x="7" y="2" width="10" height="20" rx="2"/><path d="M11 19h2"/></svg></div>
    <div><span style="font-size:14px">PHONE</span><br>(123) 456 7890</div>
  </div>
  <div class="footer-divider" style="left:718px"></div>
  <div class="footer-contact" style="left:795px">
    <div class="ring"><svg width="28" height="28" viewBox="0 0 24 24" fill="none" stroke="#fff" stroke-width="1.3"><path d="M3 10l9-6 9 6v10H3z"/><path d="M3 10l9 6 9-6"/></svg></div>
    <div><span style="font-size:14px">EMAIL</span><br>info@company.com</div>
  </div>
</footer>
<div class="abs bottom-bar">
  <div class="abs" style="left:147px;top:19px;font-size:13px">VEP</div>
  <div class="social" style="left:933px"></div>
  <div class="social" style="left:967px"></div>
  <div class="social" style="left:1001px"></div>
  <div class="social" style="left:1034px"></div>
</div>

</body>
</html>
```